25th Anniversary Fundraiser Invite and Mailing

We need an event invitation and rsvp device designed (for our members) and we have a separate letter to send out to a larger mailing list and we want the invitation information incorporated into that letter (don't need RSVP designed for that). 3 pieces (invite, rsvp and letter).

I have uploaded general info for the invite. We want business sponsors listed on the invite but are still collecting logos so it will need to be designed with space for a few more logos and a few more names - I will get those to the designer we select. The letter that was uploaded has the text we want to include but we don't necessarily want it to look like a traditional letter -- so don't feel like you have to stick with our letter head design - the logos should be in the final product but we don't need all the board member names (I can send additional logo files upon request).

The letter will need to fit into a standard envelope but doesn't have to be 8.5 x 11 - If it fits on one side great - otherwise 2 is fine. our website is www.marlowridge.org

Please refer to the attachments for the text details of the invites.

Target Market(s)

Our members and residents of our service area in the eastern panhandle of West Virginia

Industry/Entity Type

Non Profit

Requirements
Must have
• simple and elegant is generally better than busy and loud. Organizational logos - either our 25th special logo or both - which ever works best.
Nice to have
• might be interesting for the invite on the letter to be detachable -- ie you could remove the invite from the larger letter and keep on it's own.
Should not have
• anything to cutsie

```html
<!DOCTYPE html>
<html lang="en">
<head>
<meta charset="utf-8">
<title>25th Anniversary Celebration – Marlow and Stone Rivers Land Trust</title>
<link href="https://fonts.googleapis.com/css2?family=Federo&family=Josefin+Sans:wght@400;600;700&family=Cormorant+Garamond:wght@500;600&display=swap" rel="stylesheet">
<style>
  :root {
    --ink: #0e1828;
    --gold: #c9a24c;
    --gold-light: #e2c57e;
    --cream: #f1ead8;
  }
  * { margin: 0; padding: 0; box-sizing: border-box; }
  html, body { width: 880px; height: 1200px; overflow: hidden; background: var(--ink); }
  .invite {
    position: relative; width: 880px; height: 1200px; background: var(--ink);
    color: var(--gold); font-family: "Josefin Sans", sans-serif; text-align: center;
  }
  .frame { position: absolute; inset: 0; pointer-events: none; }
  .block { position: absolute; left: 0; right: 0; }
  .display { font-family: "Federo", sans-serif; text-transform: uppercase; letter-spacing: 3px; line-height: 1; }

  .join-us { top: 40px; font-size: 15px; letter-spacing: 4px; font-weight: 600; color: var(--cream); }
  .title-anniv { top: 92px; font-size: 58px; color: var(--gold-light); }
  .title-celebration { top: 158px; font-size: 66px; color: var(--gold-light); }
  .title-of { top: 232px; font-size: 16px; letter-spacing: 4px; color: var(--cream); font-weight: 600; }
  .org-name { top: 258px; font-size: 42px; color: var(--gold-light); line-height: 1.15; }

  .when-where { top: 372px; left: 70px; right: 70px; height: 94px; }
  .when { position: absolute; left: 0; top: 0; text-align: left; font-size: 30px; line-height: 1.05; color: var(--gold-light); }
  .where { position: absolute; left: 380px; top: 0; text-align: left; font-size: 22px; line-height: 1.1; color: var(--gold-light); }
  .hours { position: absolute; left: 380px; top: 56px; text-align: left; font-size: 38px; color: var(--gold-light); white-space: nowrap; }
  .rule-v { position: absolute; left: 350px; top: 0; width: 2px; height: 92px; background: var(--gold); }

  .theme { top: 486px; font-size: 22px; color: var(--gold-light); }
  .theme-sub { top: 514px; font-size: 19px; color: var(--gold-light); letter-spacing: 2px; }
  .web { top: 548px; font-size: 14px; letter-spacing: 3px; color: var(--cream); font-weight: 600; }
  .intro {
    top: 578px; left: 80px; right: 80px; font-family: "Cormorant Garamond", serif;
    font-size: 17px; line-height: 1.35; color: var(--cream); font-weight: 500;
  }

  .details { top: 720px; left: 70px; right: 70px; height: 170px; }
  .agenda, .tickets { position: absolute; top: 0; text-align: left; }
  .agenda { left: 0; width: 370px; }
  .tickets { left: 410px; right: 0; }
  .section-head { font-family: "Federo", sans-serif; font-size: 22px; letter-spacing: 3px; color: var(--gold-light); margin-bottom: 10px; }
  .agenda-list { list-style: none; }
  .agenda-list li { display: flex; font-size: 15px; font-weight: 600; letter-spacing: 1.5px; color: var(--cream); text-transform: uppercase; margin-bottom: 8px; line-height: 1.25; }
  .agenda-list .time { width: 100px; flex: none; color: var(--gold); }
  .tickets p { font-size: 15px; font-weight: 600; letter-spacing: 1.5px; color: var(--cream); text-transform: uppercase; line-height: 1.35; }
  .tickets .note { font-size: 11px; letter-spacing: 1px; color: var(--gold); margin-bottom: 6px; }
  .tickets .phone { margin-top: 8px; font-size: 17px; color: var(--gold-light); }

  .thanks { top: 958px; font-size: 22px; color: var(--gold-light); }
  .sponsor-logos { top: 1002px; left: 90px; right: 90px; display: flex; justify-content: space-between; gap: 14px; }
  .sponsor-logo {
    flex: 1; height: 66px; background: var(--cream); display: flex; align-items: center; justify-content: center;
    gap: 6px; font-size: 12px; font-weight: 700; color: var(--ink); text-transform: uppercase; letter-spacing: 0.5px; line-height: 1.15; padding: 0 6px;
  }
  .sponsor-logo .mark { width: 10px; height: 10px; background: var(--ink); flex: none; }
  .sponsor-names { top: 1110px; left: 70px; right: 70px; display: flex; justify-content: space-between; font-size: 15px; font-weight: 700; letter-spacing: 2px; color: var(--cream); }
</style>
</head>
<body>
<main class="invite">
  <svg class="frame" width="880" height="1200" viewBox="0 0 880 1200" aria-hidden="true">
    <g fill="none" stroke="#c9a24c">
      <rect x="18" y="18" width="844" height="1164" stroke-width="2"/>
      <rect x="28" y="28" width="824" height="1144" stroke-width="1"/>
      <path d="M300 30 H580 L600 50 L580 70 H300 L280 50 Z" stroke-width="1.5"/>
      <path d="M60 358 H380 M500 358 H820" stroke-width="2"/>
      <path d="M380 358 L400 348 H480 L500 358 L480 368 H400 Z" stroke-width="1.5"/>
      <path d="M60 474 H820" stroke-width="2"/>
      <path d="M60 700 H820" stroke-width="2"/>
      <path d="M60 930 H380 M500 930 H820" stroke-width="2"/>
      <path d="M380 930 L400 920 H480 L500 930 L480 940 H400 Z" stroke-width="1.5"/>
      <path d="M60 1098 H820" stroke-width="1"/>
      <path d="M28 70 H50 V50 H70 V28" stroke-width="1.5"/>
      <path d="M852 70 H830 V50 H810 V28" stroke-width="1.5"/>
      <path d="M28 1130 H50 V1150 H70 V1172" stroke-width="1.5"/>
      <path d="M852 1130 H830 V1150 H810 V1172" stroke-width="1.5"/>
    </g>
  </svg>

  <header>
    <p class="block join-us">Join us for the</p>
    <h1 class="block display title-anniv">25th Anniversary</h1>
    <p class="block display title-celebration">Celebration</p>
    <p class="block title-of">OF</p>
    <h2 class="block display org-name">Marlow and Stone Rivers<br>Land Trust</h2>
  </header>

  <section class="block when-where">
    <p class="display when">Saturday<br>September 11th<br>2015</p>
    <span class="rule-v"></span>
    <p class="display where">Historic Alder<br>Creek Mills, WV</p>
    <p class="display hours">11 AM – 4 PM</p>
  </section>

  <p class="block display theme">History and Nature</p>
  <p class="block display theme-sub">Celebrating a Generation of People Protecting Land</p>
  <p class="block web">WWW.MARLOWRIDGE.ORG</p>
  <p class="block intro">Please join us for great food, old-timey music, a live auction, and the chance to learn more about what makes the Marlow and Stone River Valley so very special. The day's activities will include a presentation by Daniel Hollis, past director of the West Virginia Chapter of The Open Land Alliance, a guided hike of Frost Ridge and the chance to tour the historic village of Alder Creek Mills.</p>

  <section class="block details">
    <div class="agenda">
      <h3 class="section-head">AGENDA</h3>
      <ul class="agenda-list">
        <li><span class="time">11 AM</span><span>Music</span></li>
        <li><span class="time">12:30 PM</span><span>Lunch and Presentations</span></li>
        <li><span class="time">1:30 PM</span><span>Live Auction</span></li>
        <li><span class="time">3 PM</span><span>Frost Ridge Hike and Historic Village Tour</span></li>
      </ul>
    </div>
    <div class="tickets">
      <h3 class="section-head">TICKETS $25</h3>
      <p class="note">Seniors and children are free</p>
      <p>Please reserve your spot by Sept 1st, 2015</p>
      <p>MRLT P.O. Box 48,<br>Holloway, WV 26777</p>
      <p class="phone">PHONE: 304-555-0142</p>
    </div>
  </section>

  <p class="block display thanks">Thank You to Our Business Sponsors</p>
  <div class="block sponsor-logos">
    <div class="sponsor-logo"><span class="mark"></span>Birchwood Bank</div>
    <div class="sponsor-logo"><span class="mark"></span>Tallow Creek Outfitters</div>
    <div class="sponsor-logo"><span class="mark"></span>Keystone Mutual</div>
    <div class="sponsor-logo"><span class="mark"></span>Ridgeline Energy</div>
    <div class="sponsor-logo"><span class="mark"></span>Fairmont Printing</div>
  </div>
  <div class="block sponsor-names">
    <span>OLD FERN TREE FARM</span>
    <span>VALLEY STONE RESTORATIONS</span>
    <span>HEARTH &amp; FIELD</span>
  </div>
</main>
</body>
</html>
```